New world-class investment firm needs a business card design

We need a business card design for a new investment firm called 'Vallin Soeurs & Company.' We acquire companies in the media sector and secure funding from conservative ultra, high-net worth individuals. We would like a black and white color design. We are seeking classic, elegant, and sophisticated designs. The final design should communicate financial safety, class, timelessness, and highly ethical. On the back of the business card, we would simply like the lion logo to be centered. I have attached a mock card, and variations on it are welcomed.
Conservative
- Garamond

```html
<!DOCTYPE html>
<html lang="en">
<head>
<meta charset="utf-8">
<title>Vallin Soeurs &amp; Company — Business Cards</title>
<link rel="stylesheet" href="https://fonts.googleapis.com/css2?family=Open+Sans:wght@400;700&display=swap">
<style>
  :root {
    --backdrop: #e3e3e1;
    --card-frame: #b6b6b6;
    --card-frame-dark: #a8a8a8;
    --tab-light: #d9d9d9;
    --ink: #1c1c1c;
    --silver: #c9c9c9;
    --panel-top: #d4d4d4;
    --panel-bottom: #b4b4b4;
    --rule: #ffffff;
    --text-dark: #2a2a2a;
    --white: #ffffff;
  }
  * { box-sizing: border-box; margin: 0; padding: 0; }
  html, body { width: 1200px; height: 1173px; overflow: hidden; }
  body { background: var(--backdrop); position: relative; }

  .card {
    position: absolute;
    top: 186px;
    width: 460px;
    height: 800px;
    padding: 28px;
    box-shadow: 0 6px 18px rgba(0,0,0,0.18);
    display: flex; flex-direction: column;
  }
  .card--front { left: 120px; background: var(--card-frame); }
  .card--back { left: 620px; background: var(--card-frame-dark); }

  .company-name {
    font-family: "Open Sans", sans-serif;
    font-weight: 400;
    font-size: 26px;
    letter-spacing: 1px;
    color: var(--silver);
    white-space: nowrap;
  }

  /* Front */
  .front-tab {
    height: 150px;
    background: var(--tab-light);
    border-top-right-radius: 44px;
    display: flex; align-items: center; justify-content: center;
  }
  .front-url {
    font-family: "Open Sans", sans-serif;
    font-size: 20px; letter-spacing: 0.5px;
    color: var(--text-dark);
  }
  .front-panel {
    flex: 1;
    background: var(--ink);
    border-bottom-left-radius: 60px;
    display: flex; justify-content: center;
    padding-top: 200px;
  }

  /* Back */
  .back-header {
    height: 150px;
    background: var(--ink);
    border-top-left-radius: 50px;
    display: flex; align-items: center; justify-content: center;
  }

  .contact-panel {
    flex: 1;
    background: linear-gradient(180deg, var(--panel-top), var(--panel-bottom));
    padding: 38px 0 0 36px;
    display: flex; flex-direction: column; gap: 26px;
  }
  .contact-row { display: flex; align-items: center; gap: 22px; }
  .contact-icon {
    width: 50px; height: 50px; flex: none;
    border-radius: 50%;
    background: var(--text-dark);
    border: 3px solid var(--panel-bottom);
    box-shadow: 0 0 0 2px var(--text-dark);
    display: flex; align-items: center; justify-content: center;
  }
  .contact-icon svg { width: 26px; height: 26px; }
  .contact-body { flex: 1; }
  .contact-text {
    font-family: "Open Sans", sans-serif;
    font-size: 17px; color: var(--text-dark);
    line-height: 1.3;
  }
  .contact-rule {
    height: 3px; background: var(--rule);
    margin-top: 20px; margin-left: -20px;
  }

  .back-footer {
    height: 170px;
    background: var(--ink);
    border-bottom-right-radius: 50px;
    display: flex; flex-direction: column; align-items: center; justify-content: center;
    font-family: "Open Sans", sans-serif; color: var(--white);
  }
  .person-name { font-size: 30px; font-weight: 700; letter-spacing: 0.5px; }
  .person-role { font-size: 26px; font-weight: 400; }
</style>
</head>
<body>

<section class="card card--front" aria-label="Card front">
  <div class="front-tab"><span class="front-url">www.vallinsoeurs.com</span></div>
  <div class="front-panel">
    <span class="company-name">Vallin Soeurs &amp; Company</span>
  </div>
</section>

<section class="card card--back" aria-label="Card back">
  <header class="back-header">
    <span class="company-name">Vallin Soeurs &amp; Company</span>
  </header>

  <div class="contact-panel">
    <div class="contact-row">
      <span class="contact-icon">
        <svg viewBox="0 0 24 24" aria-hidden="true"><path fill="#d0d0d0" d="M6.6 10.8a15.1 15.1 0 0 0 6.6 6.6l2.2-2.2c.3-.3.7-.4 1-.2 1.1.4 2.3.6 3.6.6.6 0 1 .4 1 1V20c0 .6-.4 1-1 1A17 17 0 0 1 3 4c0-.6.4-1 1-1h3.5c.6 0 1 .4 1 1 0 1.3.2 2.5.6 3.6.1.3 0 .7-.2 1z"/></svg>
      </span>
      <div class="contact-body">
        <p class="contact-text">+44 207 946 01</p>
        <div class="contact-rule"></div>
      </div>
    </div>
    <div class="contact-row">
      <span class="contact-icon">
        <svg viewBox="0 0 24 24" aria-hidden="true"><rect x="3" y="6" width="18" height="12" fill="#d0d0d0"/><path d="M3 6l9 7 9-7" fill="none" stroke="#2a2a2a" stroke-width="1.6"/></svg>
      </span>
      <div class="contact-body">
        <p class="contact-text">hello@vallinsoeurs.com</p>
        <div class="contact-rule"></div>
      </div>
    </div>
    <div class="contact-row">
      <span class="contact-icon">
        <svg viewBox="0 0 24 24" aria-hidden="true" fill="none" stroke="#d0d0d0" stroke-width="1.6"><circle cx="12" cy="12" r="9"/><ellipse cx="12" cy="12" rx="4" ry="9"/><path d="M3 12h18M4.5 7.5h15M4.5 16.5h15"/></svg>
      </span>
      <div class="contact-body">
        <p class="contact-text">www.vallinsoeurs.com</p>
        <div class="contact-rule"></div>
      </div>
    </div>
    <div class="contact-row">
      <span class="contact-icon">
        <svg viewBox="0 0 24 24" aria-hidden="true"><path fill="#d0d0d0" d="M12 2a7 7 0 0 0-7 7c0 5.2 7 13 7 13s7-7.8 7-13a7 7 0 0 0-7-7zm0 9.5A2.5 2.5 0 1 1 12 6.5a2.5 2.5 0 0 1 0 5z"/></svg>
      </span>
      <div class="contact-body">
        <p class="contact-text">Suite 210, Hale House, UK, W1K 4PL<br>18 Carrow Lane West</p>
        <div class="contact-rule"></div>
      </div>
    </div>
  </div>

  <footer class="back-footer">
    <span class="person-name">ELISE VALLIN</span>
    <span class="person-role">Founder</span>
  </footer>
</section>

</body>
</html>
```